Wordpress theme for new e-commerce tropical furniture manufacturing business

We want to develop a Wordpress theme to suit our new Reefline Furniture website currently under development, business details as below.
Please see attached logo design for ideas of the design. This logo will be used as - letterhead, business cards, furniture labels etc.
We are a small Australian family business that provides products as below:
- Hand Crafted, Creative Tropical design Furniture,
(manufacture and sales).
- Specializing in mirror- wall art
- One off – designs 'made to order'.
- Individually badged pieces, each with an identification production number.
Materials used that may be incorporated in the 'web theme designs' are: Bamboo, Wood, Waves, Ocean, Shells, Tropical flowers (eg; Hibiscus, Frangipani, Heliconias, Stralitzias), Palms,Pandanus & Stone etc. etc.
Industry/Entity Type
E-Commerce
Colors
Designer to choose colors to be used in the design.
Look and feel
Each slider illustrates characteristics of the customer's brand and the style your logo design should communicate.

```html
<!DOCTYPE html>
<html lang="en">
<head>
<meta charset="utf-8">
<title>Reefline Furniture</title>
<link href="https://fonts.googleapis.com/css2?family=Roboto:wght@400;500;700;900&family=Dancing+Script:wght@500&display=swap" rel="stylesheet">
<style>
:root{
  --bamboo-dark:#4a3018;
  --bamboo-mid:#a27a3c;
  --wood-header:#4b2f1c;
  --wood-header-light:#6a4428;
  --page-white:#ffffff;
  --page-tan:#e4bd85;
  --brown:#8a6232;
  --brown-title:#9a6f3e;
  --ink:#111111;
  --sidebar:#3f4649;
  --ocean:#3a8fcf;
  --ocean-light:#9fd3ee;
  --cream:#f3ece0;
  --footer-text:#fff6e6;
}
*{box-sizing:border-box;margin:0;padding:0}
html,body{width:1086px;height:1200px;overflow:hidden}
body{position:relative;font-family:Arial,Helvetica,sans-serif;color:var(--ink)}
.backdrop{position:absolute;inset:0;
  background:
   radial-gradient(circle at 8% 78%,rgba(40,150,220,.55),transparent 16%),
   radial-gradient(circle at 96% 40%,rgba(40,150,220,.5),transparent 14%),
   radial-gradient(circle at 95% 58%,rgba(230,190,40,.55),transparent 12%),
   radial-gradient(circle at 12% 10%,rgba(70,130,50,.5),transparent 18%),
   radial-gradient(circle at 90% 8%,rgba(70,130,50,.5),transparent 16%),
   repeating-linear-gradient(90deg,var(--bamboo-dark) 0 8px,var(--bamboo-mid) 8px 60px,#c89a55 60px 80px,var(--bamboo-mid) 80px 120px,var(--bamboo-dark) 120px 130px);}
.accent-shell{position:absolute;left:48px;top:1058px;width:156px;height:142px;border-radius:50% 50% 40% 40%;background:radial-gradient(circle at 50% 70%,#f4d2b6,#d6835d)}
.accent-flower{position:absolute;left:820px;top:1016px;width:230px;height:184px;border-radius:50%;background:radial-gradient(circle,#f3b81c 20%,#fbe27a 55%,rgba(251,226,122,0) 72%)}

.header{position:absolute;left:156px;top:0;width:774px;height:84px;
  background:linear-gradient(180deg,var(--wood-header-light),var(--wood-header));
  box-shadow:0 3px 8px rgba(0,0,0,.5)}
.phone{position:absolute;left:22px;top:14px;display:flex;align-items:center;gap:8px;color:#e6c99a;font-family:Roboto,sans-serif;font-size:13.5px}
.top-links{position:absolute;right:25px;top:19px;display:flex;gap:16px;color:#e6c99a;font-family:Roboto,sans-serif;font-size:9px;text-transform:uppercase}
.main-nav{position:absolute;top:52px;left:0;width:100%;font-family:Roboto,sans-serif;font-weight:700;font-size:14px;color:#fff}
.main-nav a{position:absolute;color:#fff;text-decoration:none;white-space:nowrap}

.page{position:absolute;left:156px;top:384px;width:774px;height:732px;background:var(--page-white);box-shadow:0 0 10px rgba(0,0,0,.4)}
.page-inner{position:absolute;left:8px;top:0;width:758px;height:724px;background:var(--page-tan)}

.slider{position:absolute;left:150px;top:106px;width:830px;height:298px;border:7px solid #d9d3c7;border-radius:12px 30px 14px 18px;
  background:linear-gradient(180deg,#6fb2e6 0%,#3a8fcf 40%,#5a3c22 62%,#2a5f86 80%,#3f8dc0 100%);box-shadow:0 4px 10px rgba(0,0,0,.45)}
.tagline{position:absolute;left:56px;top:224px;font-family:"Dancing Script",cursive;font-size:31px;color:#fff;white-space:nowrap}
.slider-dots{position:absolute;right:40px;top:244px;display:flex;gap:3px}
.slider-dots span{width:7px;height:7px;border-radius:50%;background:#b9c8d2}
.slider-dots span:first-child{background:#fff}

.hanger{position:absolute;left:170px;top:60px;overflow:visible}
.logo-sign{position:absolute;left:164px;top:140px;width:234px;height:140px;background:#fff;border:5px solid #c99a5c;border-radius:4px;box-shadow:0 3px 6px rgba(0,0,0,.35);text-align:center}
.logo-name{margin-top:44px;font-family:Roboto,sans-serif;font-weight:700;font-size:21px;color:#2a8fcc}
.logo-url{margin-top:8px;font-family:Roboto,sans-serif;font-size:8px;color:#666;letter-spacing:.5px}

.welcome{position:absolute;left:172px;top:440px;width:520px;text-align:center}
.welcome-kicker{font-family:Roboto,sans-serif;font-weight:900;font-size:19px;display:flex;justify-content:center;align-items:center;gap:10px}
.welcome-kicker .dots{width:86px;height:8px;background:radial-gradient(circle,#b59a70 1px,transparent 1.5px) 0 0/4px 4px}
.welcome-title{margin-top:8px;font-family:Roboto,sans-serif;font-weight:700;font-size:31px;color:var(--brown)}
.welcome-text{position:absolute;left:172px;top:523px;width:516px;text-align:center;font-size:10.5px;line-height:18px}

.ribbon{position:absolute;left:326px;top:602px}
.ribbon-label{position:absolute;left:356px;top:620px;width:136px;text-align:center;font-family:Roboto,sans-serif;font-weight:700;font-size:15px;color:#ecd7b4}

.product{position:absolute;top:696px;width:158px;text-align:center}
.photo{display:block;width:158px;height:122px;border:4px solid #fff}
.product h3{margin-top:16px;font-family:Roboto,sans-serif;font-weight:700;font-size:16px;color:var(--brown-title)}
.product p{margin-top:9px;font-size:9.3px;line-height:17px}
.read-more{display:inline-block;margin-top:14px;padding:4px 12px;font-family:Roboto,sans-serif;font-weight:500;font-size:10px;text-transform:uppercase;text-decoration:none;color:#9a6f3e;background:#e9d5b0;border:2px solid #8a6232;box-shadow:-2px 2px 0 #8a6232}

.sidebar{position:absolute;left:721px;top:430px;width:197px;height:555px;background:var(--sidebar);text-align:center}
.polaroid{position:absolute;background:#f2f0ea;box-shadow:0 3px 6px rgba(0,0,0,.5)}
.polaroid .pic{position:absolute;left:9px;top:9px}
.polaroid .caption{position:absolute;left:0;width:100%;font-family:Roboto,sans-serif;font-weight:700;color:#222}
.sidebar-text{position:absolute;left:14px;top:198px;width:170px;font-size:9.3px;line-height:17px;color:#fff}
.sidebar .read-more{position:absolute;left:53px;top:296px;margin:0;color:#fff;background:var(--sidebar);border-color:#fff;box-shadow:-2px 2px 0 #fff}

.footer{position:absolute;left:172px;top:1018px;width:742px;height:90px;background:var(--brown)}
.footer-nav{position:absolute;left:27px;top:24px;font-family:Roboto,sans-serif;font-size:9px;color:var(--footer-text);text-transform:uppercase}
.footer-nav a{position:absolute;color:var(--footer-text);text-decoration:none;white-space:nowrap}
.copyright{position:absolute;left:27px;top:45px;font-family:Roboto,sans-serif;font-size:9px;color:var(--footer-text);white-space:nowrap}
.social{position:absolute;top:24px;left:584px;display:flex;gap:7px}
.social span{width:30px;height:30px;border-radius:50%;border:1.5px solid #e6cfa8}
</style>
</head>
<body>
<div class="backdrop" role="img" aria-label="Bamboo pole wall with palm fronds, blue water splashes and a striped beach ball"></div>
<div class="accent-shell" role="img" aria-label="Scallop sea shell"></div>
<div class="accent-flower" role="img" aria-label="Yellow frangipani flower"></div>

<header class="header">
  <div class="phone">
    <svg width="24" height="24" viewBox="0 0 24 24" aria-hidden="true"><circle cx="12" cy="12" r="11" fill="none" stroke="#e6c99a" stroke-width="1.5"/><path d="M8 6c-1 1-1 3 1 6s4 5 6 5l1.5-1.5-2-2-1.3.8c-1-.6-2.2-2-2.8-3l.8-1.3-2-2z" fill="#e6c99a"/></svg>
    <span>CALL US : ( 1300 ) 555 018</span>
  </div>
  <nav class="top-links"><span>My Account</span><span>|</span><span>My Cart</span><span>|</span><span>Your Cart is : 0 Items</span></nav>
  <nav class="main-nav">
    <a style="left:165px">HOME</a>
    <a style="left:265px">ABOUT US</a>
    <a style="left:393px">PRODUCTS</a>
    <a style="left:525px">SERVICES</a>
    <a style="left:649px">CONTACT US</a>
  </nav>
</header>

<div class="page"><div class="page-inner"></div></div>

<section class="slider" role="img" aria-label="Overwater bungalows lit at dusk over a calm blue lagoon">
  <div class="tagline">We are a small Australian family business</div>
  <div class="slider-dots"><span></span><span></span><span></span><span></span></div>
</section>

<svg class="hanger" width="240" height="100" aria-hidden="true">
  <line x1="110" y1="6" x2="8" y2="93" stroke="#333" stroke-width="1.5"/>
  <line x1="110" y1="6" x2="213" y2="93" stroke="#333" stroke-width="1.5"/>
  <circle cx="110" cy="6" r="7" fill="#ccc" stroke="#555"/>
</svg>
<div class="logo-sign">
  <div class="logo-name">Reefline Furniture</div>
  <div class="logo-url">www.reeflinefurniture.com.au</div>
</div>

<section class="welcome">
  <div class="welcome-kicker"><span class="dots"></span>WELCOME TO<span class="dots"></span></div>
  <h1 class="welcome-title">REEFLINE FURNITURE</h1>
</section>
<p class="welcome-text">Many desktop publishing packages and web page editors now use Lorem Ipsum as their default model text, and a search for 'lorem ipsum' will uncover many web sites still in their infancy. Various versions have evolved over the years, sometimes by accident, sometimes on purpose</p>

<svg class="ribbon" width="196" height="66" aria-hidden="true">
  <path d="M20 30 L38 28 L36 62 L2 64 L14 50 Z" fill="#8a6232"/>
  <path d="M168 2 L194 2 L184 20 L192 36 L170 38 Z" fill="#8a6232"/>
  <path d="M32 16 L172 12 L168 50 L30 54 Z" fill="#9a7040"/>
</svg>
<div class="ribbon-label">PRODUCTS</div>

<article class="product" style="left:185px">
  <span class="photo" role="img" aria-label="Beach umbrella and wooden chairs on white sand by turquoise sea" style="background:linear-gradient(180deg,#2f86d0,#5cc6d8 55%,#f1ead8 70%)"></span>
  <h3>HAND CRAFTED</h3>
  <p>Many desktop publishing packages and web page editors now use Lorem Ipsum as their default model text, and a search...</p>
  <a class="read-more">Read More</a>
</article>
<article class="product" style="left:366px">
  <span class="photo" role="img" aria-label="Pink and yellow frangipani flower among green leaves" style="background:radial-gradient(circle at 55% 60%,#f2b8c8 10%,#2f6b2a 45%,#183d17)"></span>
  <h3>TROPICAL</h3>
  <p>Many desktop publishing packages and web page editors now use Lorem Ipsum as their default model text, and a search...</p>
  <a class="read-more">Read More</a>
</article>
<article class="product" style="left:544px">
  <span class="photo" role="img" aria-label="Two cream sea shells on brown sand" style="background:radial-gradient(circle at 50% 50%,#e8dcc6 20%,#8c6a52 60%)"></span>
  <h3>SHELLS</h3>
  <p>Many desktop publishing packages and web page editors now use Lorem Ipsum as their default model text, and a search...</p>
  <a class="read-more">Read More</a>
</article>

<aside class="sidebar">
  <div class="polaroid" style="left:19px;top:14px;width:162px;height:174px">
    <span class="pic" role="img" aria-label="Deck chairs under a yellow umbrella on a sunny beach" style="width:144px;height:112px;background:linear-gradient(180deg,#5fb4ea,#3aa2c8 55%,#e9dcc4 70%)"></span>
    <div class="caption" style="top:135px;font-size:16px">ABOUT US</div>
  </div>
  <p class="sidebar-text">Many desktop publishing packages and web page editors now use Lorem Ipsum as their default model text, and a search for 'lorem ipsum' will uncover many...</p>
  <a class="read-more">Read More</a>
  <div class="polaroid" style="left:16px;top:352px;width:168px;height:172px;transform:rotate(-3deg)">
    <span class="pic" role="img" aria-label="Assorted sea shells arranged on sand" style="width:150px;height:124px;background:radial-gradient(circle,#d9b592 20%,#b48b66 70%)"></span>
    <div class="caption" style="top:142px;font-size:13px">PHOTO GALLERY</div>
  </div>
</aside>

<footer class="footer">
  <nav class="footer-nav">
    <a style="left:0">Home</a>
    <a style="left:55px">About Us</a>
    <a style="left:128px">Products</a>
    <a style="left:203px">Services</a>
    <a style="left:274px">Contact Us</a>
  </nav>
  <p class="copyright">COPYRIGHT © REEFLINE FURNITURE 2014. ALL RIGHTS RESERVED.</p>
  <div class="social" aria-label="Social links"><span></span><span></span><span></span><span></span></div>
</footer>
</body>
</html>
```